Website Header Development

I am after a redesign of the Header of a website www.qlvoltrix.com.au.
This project is for the header only, and should fit in with the rest of the site
Target Market(s)
Business
Requirements
Should not have
- Over the top. Keep it simple

```html
<!DOCTYPE html>
<html lang="en">
<head>
<meta charset="utf-8">
<title>Qlvoltrix Energy – Header</title>
<link rel="stylesheet" href="https://fonts.googleapis.com/css2?family=Open+Sans:wght@600&display=swap">
<style>
  :root {
    --band-dark: #6fa872;
    --band-mid: #82b784;
    --band-light: #9cc79b;
    --sweep: rgba(255, 255, 255, 0.12);
    --sweep-edge: rgba(255, 255, 255, 0.35);
    --brand-navy: #1f3a8f;
  }
  html, body {
    margin: 0;
    padding: 0;
    overflow: hidden;
  }
  .site-header {
    position: relative;
    width: 1200px;
    height: 138px;
    overflow: hidden;
    background: linear-gradient(100deg, var(--band-dark) 0%, var(--band-mid) 55%, var(--band-light) 100%);
  }
  .header-sweep {
    position: absolute;
    inset: 0;
    width: 1200px;
    height: 138px;
  }
  .brand-name {
    position: absolute;
    left: 48px;
    top: 56px;
    margin: 0;
    font-family: "Open Sans", sans-serif;
    font-weight: 600;
    font-size: 31px;
    line-height: 1;
    letter-spacing: -0.2px;
    color: var(--brand-navy);
  }
</style>
</head>
<body>
  <header class="site-header">
    <svg class="header-sweep" viewBox="0 0 1200 138" aria-hidden="true">
      <path d="M0 0 H1200 V0 H1150 C1000 40 700 110 0 130 Z" fill="var(--sweep)"/>
      <path d="M1150 0 C1000 40 700 110 0 130" fill="none" stroke="var(--sweep-edge)" stroke-width="1.5"/>
    </svg>
    <p class="brand-name">qlvoltrix energy</p>
  </header>
</body>
</html>
```